Digital Marketing Website Design

I need the homepage designed for my new digital marketing agency I am starting. The main goal for this homepage is to drive people to make an appointment for me to discuss their upcoming projects. Here are some examples of the layouts that I would like to emulate.
https://www.tallorchard.com/
https://www.webmerchantry.com/
https://talewick.com/
https://drmevorran.com/
https://www.neatlynestled.org/
My main focus is to attract leads that need help with running digital ads such as Chatterbook ads and Quorix Ads. I do offer other services like SEO and other things but the main focus is digital Ads.
The final design should communicate Ember Pixelry is a Digital marketing strategist building predictable revenue for small businesses through digital ads, email and marketing automation.
Target Market(s)
30-55, business owners, income 100K+, ecommerce companies, etc.
Industry/Entity Type
Digital Marketing
Number of Pages Required
2 page
Requirements
Must have
- An appealing look and feel set to drive people to make an appointment.
There needs to be a call to action button in the far right of the navigation
The same call to action in the navigation needs to be in each section on the homepage.
I need the homepage and an about us page.

```html
<!DOCTYPE html>
<html lang="en">
<head>
<meta charset="utf-8">
<title>Ember Pixelry — Digital Ads for Small Businesses</title>
<link href="https://fonts.googleapis.com/css2?family=Poppins:ital,wght@0,300;0,400;0,500;0,600;0,700;1,300&display=swap" rel="stylesheet">
<style>
:root{
  --orange:#f7941d;
  --orange-deep:#ef5a28;
  --ink:#111111;
  --text:#555555;
  --partner:#333333;
  --peach:#fbe8d0;
  --grey-band:#f5f5f5;
  --line:#e6e6e6;
  --white:#ffffff;
  --star:#f7941d;
}
*{box-sizing:border-box;margin:0;padding:0}
html,body{width:1200px;height:3661px;overflow:hidden}
body{font-family:'Poppins',sans-serif;color:var(--text);background:var(--white);position:relative}
section,header,footer{position:absolute;left:0;width:1200px}
.abs{position:absolute}
.center{text-align:center}
.media{position:absolute}

/* Hero */
.hero{top:0;height:677px;background:linear-gradient(180deg,var(--orange) 0%,#f4782a 60%,var(--orange-deep) 100%);overflow:hidden}
.brand{left:78px;top:26px;color:var(--white);font-weight:700;font-size:27px;letter-spacing:-0.5px}
.nav-link{position:absolute;top:38px;color:var(--white);font-size:15px;text-decoration:none}
.btn-outline{position:absolute;left:884px;top:21px;width:239px;height:52px;border:1.5px solid var(--white);border-radius:26px;color:var(--white);font-size:14px;font-weight:500;display:flex;align-items:center;justify-content:center}
.hero-title{left:350px;width:500px;top:196px;color:var(--white);font-weight:600;font-size:40px;line-height:48px}
.hero-sub{left:360px;width:480px;top:350px;color:var(--white);font-size:16px;line-height:27px;font-family:Arial,sans-serif}
.btn-white{left:480px;top:429px;width:240px;height:56px;border-radius:28px;background:var(--white);color:var(--orange-deep);font-size:15px;font-weight:500;display:flex;align-items:center;justify-content:center}
.hero-link{left:400px;width:400px;top:514px;color:var(--white);font-size:15px;font-weight:500}

/* How it works */
.h2{position:absolute;left:0;width:1200px;text-align:center;color:var(--ink);font-weight:600;font-size:40px;letter-spacing:-0.5px}
.how{top:677px;height:834px}
.how-copy{left:640px;top:152px;width:432px;font-size:14.5px;line-height:26px;color:var(--text)}
.how-copy p+p{margin-top:24px}
.step-icon{width:104px;height:104px;border-radius:50%;background:var(--white);box-shadow:0 4px 14px rgba(0,0,0,.1)}
.step-text{font-size:14.5px;line-height:27px;color:var(--text)}

/* Note band */
.note{top:1511px;height:229px;background:var(--peach)}
.note-box{left:183px;top:43px;width:834px;height:139px;background:var(--white);font-size:15.5px;line-height:27px;color:#222;display:flex;align-items:center;justify-content:center;padding:0 70px}

/* Partners */
.partners{top:1740px;height:454px}
.partner{position:absolute;display:flex;align-items:center;justify-content:center;font-weight:600;font-size:24px;color:var(--partner)}

/* Testimonial */
.quotes{top:2194px;height:482px;background:var(--grey-band)}
.quote-text{left:210px;width:780px;top:242px;font-style:italic;font-weight:300;font-size:16px;line-height:29px;color:#555}

/* Fundamentals */
.fund{top:2676px;height:392px;overflow:hidden}
.btn-grad{left:465px;top:230px;width:270px;height:57px;border-radius:29px;background:linear-gradient(90deg,var(--orange-deep),var(--orange));color:var(--white);font-size:15px;font-weight:500;display:flex;align-items:center;justify-content:center}

/* Reach */
.reach{top:3068px;height:522px;background:linear-gradient(180deg,var(--orange) 0%,#f4782a 55%,var(--orange-deep) 100%)}
.reach-title{left:0;width:1200px;top:66px;color:var(--white);font-weight:600;font-size:40px;letter-spacing:-0.5px}
.contact-box{left:121px;top:155px;width:958px;height:292px;background:var(--white)}
.col{position:absolute;top:48px;width:300px;text-align:center}
.col h3{font-weight:500;font-size:19px;color:var(--ink);margin-bottom:18px}
.col p{font-size:14.5px;line-height:27px;color:#444}
.col .gap{height:27px}
.divider{position:absolute;top:50px;width:1px;height:200px;background:var(--line)}

/* Footer */
.footer{top:3590px;height:71px;background:var(--white)}
.social{position:absolute;top:14px;width:46px;height:46px;border:1.5px solid var(--orange);border-radius:50%;color:var(--orange);font-size:16px;font-weight:500;display:flex;align-items:center;justify-content:center}
</style>
</head>
<body>

<header class="hero">
  <div class="abs brand">EMBER PIXELRY</div>
  <nav>
    <a class="nav-link" style="left:610px">Home</a>
    <a class="nav-link" style="left:686px">How it Work</a>
    <a class="nav-link" style="left:797px">Contact</a>
    <a class="btn-outline">SCHEDULE APPOINTMENT</a>
  </nav>

  <div class="media" role="img" aria-label="Laptop, stylus and earphones on the desk" style="left:0;top:213px;width:370px;height:440px;background:radial-gradient(ellipse at 25% 40%,rgba(40,40,45,.55),rgba(40,40,45,0) 65%)"></div>
  <div class="media" role="img" aria-label="Tablet showing a street photo" style="left:924px;top:303px;width:276px;height:374px;background:linear-gradient(160deg,#f4f4f4,#dcdcdc);border-radius:24px 0 0 0"></div>
  <div class="media" role="img" aria-label="Phone showing the agency website" style="left:775px;top:387px;width:218px;height:290px;background:linear-gradient(160deg,#fafafa,#e2e2e2);border-radius:24px 24px 0 0;box-shadow:0 4px 14px rgba(0,0,0,.12)"></div>

  <h1 class="abs hero-title center">We Built Profitable Ad Campaigns For small businesses</h1>
  <p class="abs hero-sub center">The selling system that brings in Predictable revenue through digital ads, email, and marketing automation.</p>
  <a class="abs btn-white">FREE CHATTERBOOK ADS</a>
  <a class="abs hero-link center">SCHEDULE APPOINTMENT</a>
</header>

<section class="how">
  <h2 class="h2" style="top:68px">HOW IT WORK</h2>
  <div class="media" role="img" aria-label="Tablet, keyboard, coffee cup and glasses on a white desk with leaves" style="left:122px;top:158px;width:484px;height:301px;background:linear-gradient(135deg,#2f5f2a 0%,#e9ecea 35%,#f2f2f2 70%,#d8d8d8 100%)"></div>
  <div class="abs how-copy">
    <p>At Ember Pixelry Solutions we know that you want to have a profitable business. In order to do that, you need a strong system that can predictably bring in sales even in bad times. The problem is there is so much out there to wade through and so many people telling you what you should do which makes you feel frustrated, lost, and flat out stressed out. We believe that businesses with great products should get the customer.</p>
    <p>We understand the frustration which is why we are here to help you maneuver through the minutiae and create a system that flat out works.</p>
  </div>

  <div class="abs step-icon" style="left:205px;top:522px">
    <svg width="104" height="104" viewBox="0 0 104 104" fill="none" stroke="#ef5a28" stroke-width="2">
      <rect x="36" y="30" width="38" height="34" rx="3"/><line x1="36" y1="40" x2="74" y2="40"/>
      <line x1="48" y1="40" x2="48" y2="64"/><line x1="61" y1="40" x2="61" y2="64"/><line x1="36" y1="52" x2="74" y2="52"/>
      <path d="M28 50c0 14 10 26 24 26l4-6-6-5-4 3c-5-3-8-7-10-11l3-4-5-6z"/>
    </svg>
  </div>
  <div class="abs step-icon" style="left:548px;top:522px">
    <svg width="104" height="104" viewBox="0 0 104 104" fill="none" stroke="#ef5a28" stroke-width="2">
      <circle cx="52" cy="52" r="22"/><circle cx="52" cy="46" r="6"/><path d="M41 64c2-7 20-7 22 0"/>
      <circle cx="52" cy="24" r="4"/><circle cx="78" cy="52" r="4"/><circle cx="26" cy="52" r="4"/><circle cx="52" cy="80" r="4"/>
    </svg>
  </div>
  <div class="abs step-icon" style="left:883px;top:522px">
    <svg width="104" height="104" viewBox="0 0 104 104" fill="none" stroke="#ef5a28" stroke-width="2">
      <circle cx="56" cy="30" r="9"/><text x="52" y="35" font-size="13" fill="#ef5a28" stroke="none" font-family="Poppins,sans-serif">$</text>
      <rect x="38" y="46" width="36" height="18" rx="2" transform="rotate(-25 56 55)"/>
      <path d="M26 64l14 14h24l10-8"/>
    </svg>
  </div>
  <p class="abs step-text center" style="left:120px;width:280px;top:652px">Schedule an appointment to go through the basics of what you need and to find out if we are a good fit to work together.</p>
  <p class="abs step-text center" style="left:460px;width:280px;top:652px">Work with our team to build out your customer journey and selling system</p>
  <p class="abs step-text center" style="left:830px;width:220px;top:652px">Execute and enjoy the extra revenue!</p>
</section>

<section class="note">
  <div class="abs note-box center">So, schedule your appointment today. And in the meantime, checkout our Chatterbook ads checklist. So you can stop any poor running campaigns and fill in the gaps where they are needed.</div>
</section>

<section class="partners">
  <h2 class="h2" style="top:64px">TRUSTED PARTNER</h2>
  <div class="abs" style="left:490px;top:162px;width:1px;height:217px;background:var(--line)"></div>
  <div class="abs" style="left:715px;top:162px;width:1px;height:217px;background:var(--line)"></div>
  <div class="abs" style="left:286px;top:275px;width:624px;height:1px;background:var(--line)"></div>
  <div class="partner" style="left:286px;top:162px;width:204px;height:113px">Lumora</div>
  <div class="partner" style="left:490px;top:162px;width:225px;height:113px">Quorix Ads</div>
  <div class="partner" style="left:715px;top:162px;width:195px;height:113px">Vantrel</div>
  <div class="partner" style="left:286px;top:276px;width:204px;height:103px">Chatterbook</div>
  <div class="partner" style="left:490px;top:276px;width:225px;height:103px">Notionly</div>
  <div class="partner" style="left:715px;top:276px;width:195px;height:103px">Sonavey</div>
</section>

<section class="quotes">
  <h2 class="h2" style="top:58px">WHAT OTHER ARE SAYING</h2>
  <div class="abs" style="left:566px;top:134px;width:68px;height:68px;border-radius:50%;background:linear-gradient(180deg,var(--orange),var(--orange-deep));color:#fff;font-size:52px;font-weight:700;line-height:86px;text-align:center">&ldquo;</div>
  <svg class="abs" style="left:98px;top:228px" width="22" height="40" viewBox="0 0 22 40" fill="none" stroke="#bbb" stroke-width="1.5"><path d="M18 2L4 20l14 18"/></svg>
  <svg class="abs" style="left:1078px;top:228px" width="22" height="40" viewBox="0 0 22 40" fill="none" stroke="#bbb" stroke-width="1.5"><path d="M4 2l14 18L4 38"/></svg>
  <p class="abs quote-text center">Lorem Ipsum is simply dummy text of the printing and typesetting industry. Lorem Ipsum has been the industry's standard dummy text ever since the 1500s, when an unknown printer took a galley of type and scrambled it to make a type specimen book.</p>
  <div class="abs center" style="left:0;width:1200px;top:342px;color:var(--star);font-size:22px;letter-spacing:4px">★★★★★</div>
  <p class="abs center" style="left:0;width:1200px;top:389px;font-size:16px;color:#222">Client Name , Loremipsum Simple text</p>
</section>

<section class="fund">
  <div class="media" role="img" aria-label="Laptop and stylus" style="left:0;top:68px;width:249px;height:256px;background:radial-gradient(ellipse at 30% 45%,rgba(40,40,45,.55),rgba(40,40,45,0) 68%)"></div>
  <div class="media" role="img" aria-label="White earphones" style="left:1080px;top:-10px;width:120px;height:192px;background:radial-gradient(ellipse at 60% 45%,rgba(200,200,200,.6),rgba(255,255,255,0) 70%)"></div>
  <div class="media" role="img" aria-label="Phone showing the agency website" style="left:880px;top:189px;width:320px;height:203px;background:linear-gradient(160deg,#f2f2f2,#dadada);border-radius:40px 0 0 0"></div>
  <h2 class="h2" style="top:96px">THE FUNDAMENTALS</h2>
  <p class="abs center" style="left:350px;width:500px;top:164px;font-size:16px;line-height:27px;color:#555">people to make an appointment for me to discuss their upcoming projects</p>
  <a class="abs btn-grad">SCHEDULE APPOINTMENT</a>
</section>

<section class="reach">
  <h2 class="abs reach-title center">YOU CAN ALSO REACH US</h2>
  <div class="abs contact-box">
    <div class="col" style="left:16px">
      <h3>ADDREES</h3>
      <p>EmberPixelry</p>
      <p>101 - Lorem ipsum simple</p>
      <p>text print type text</p>
    </div>
    <div class="divider" style="left:334px"></div>
    <div class="col" style="left:328px">
      <h3>CONTACT INFO</h3>
      <p>Phone :</p>
      <p>123 456 7890</p>
      <div class="gap"></div>
      <p>Email :</p>
      <p>info@emberpixelry.com</p>
    </div>
    <div class="divider" style="left:625px"></div>
    <div class="col" style="left:628px">
      <h3>QUICKLINKS</h3>
      <p>Terms of Service</p>
      <p>Privacy Policy</p>
      <p>expanded navigation</p>
      <p>flagship content</p>
      <p>case studies</p>
    </div>
  </div>
</section>

<footer class="footer">
  <p class="abs" style="left:80px;top:27px;font-size:14.5px;color:#222">©EmberPixelry - 2020 All rights Reserved.</p>
  <a class="social" style="left:1025px" aria-label="Chatterbook">C</a>
  <a class="social" style="left:1076px" aria-label="Chirply">C</a>
</footer>

</body>
</html>
```